Fenmoor Business Card

I want a business card for me and my employees.
On one side it must be in Greek and on the other side in English. The color must much the one of the logo

Target Market(s)

Customers that are looking for security and antipiracy advisors

Contact Information for Business Card

Title, Email, Phone, website , Mobile Address Zip code, city and country

Requirements
Must have
• The colors of our logo (the blue ones)

```html
<!DOCTYPE html>
<html lang="en">
<head>
<meta charset="utf-8">
<title>Fenmoor Advisory – Business Cards</title>
<link rel="stylesheet" href="https://fonts.googleapis.com/css2?family=Open+Sans:wght@400;600;700;800&display=swap">
<style>
  :root {
    --stage: #232323;
    --card: #ffffff;
    --navy: #27275f;
    --lavender: #dcdbe6;
    --ink: #1c1c24;
  }
  * { box-sizing: border-box; margin: 0; padding: 0; }
  html, body { width: 1200px; height: 780px; overflow: hidden; background: var(--stage); }
  .canvas {
    width: 1200px; height: 780px;
    display: flex; justify-content: center; align-items: center; gap: 90px;
    font-family: "Open Sans", sans-serif;
  }
  .card {
    position: relative;
    width: 340px; height: 600px;
    background: var(--card);
    border-radius: 24px;
    overflow: hidden;
    color: var(--ink);
  }
  .brand-field {
    position: absolute; left: 0; top: 60px;
    width: 226px; height: 260px;
    background: var(--lavender);
  }
  .brand-field::after {
    content: ""; position: absolute; left: 34px; top: 34px; right: 34px; bottom: 34px;
    background: var(--card);
  }
  .wordmark {
    position: absolute; right: 18px; top: 22px;
    width: 66px; height: 250px;
  }
  .wordmark-lockup {
    position: absolute; left: 0; top: 250px;
    width: 250px; height: 66px;
    display: flex; align-items: center; gap: 10px;
    transform: rotate(-90deg); transform-origin: top left;
  }
  .wordmark-square { flex: none; width: 40px; height: 40px; background: var(--navy); }
  .wordmark-text { display: flex; flex-direction: column; line-height: 1; }
  .wordmark-name {
    font-weight: 800; font-size: 32px; letter-spacing: 1px;
    color: var(--navy); text-transform: uppercase;
  }
  .wordmark-sub {
    font-weight: 400; font-size: 17px; letter-spacing: 8px;
    color: var(--navy); text-transform: uppercase; margin-top: 4px;
  }
  .holder { position: absolute; left: 0; right: 0; top: 346px; text-align: center; }
  .holder-name { font-weight: 800; font-size: 27px; color: var(--navy); line-height: 1.15; }
  .holder-title { font-weight: 700; font-size: 14px; color: var(--ink); margin-top: 2px; }
  .dot-row { position: absolute; left: 20px; width: 300px; height: 26px; }
  .dot-row--contact { top: 410px; }
  .dot-row--address { top: 518px; }
  .contact-list {
    position: absolute; left: 0; right: 0; top: 440px;
    list-style: none; text-align: center;
    font-size: 14px; line-height: 19px; color: var(--ink);
  }
  .address {
    position: absolute; left: 0; right: 0; top: 548px;
    font-style: normal; text-align: center;
    font-size: 13px; line-height: 18px; color: var(--ink);
  }
  .dot { fill: var(--navy); }
  .glyph { stroke: var(--card); fill: none; stroke-width: 1.4; stroke-linecap: round; stroke-linejoin: round; }
</style>
</head>
<body>
<main class="canvas">

  <article class="card card--english" lang="en">
    <div class="brand-field" role="img" aria-label="Faint brand backdrop area"></div>
    <div class="wordmark">
      <div class="wordmark-lockup">
        <span class="wordmark-square"></span>
        <div class="wordmark-text">
          <span class="wordmark-name">Fenmoor</span>
          <span class="wordmark-sub">Advisory</span>
        </div>
      </div>
    </div>
    <header class="holder">
      <h1 class="holder-name">Daria Velkova</h1>
      <p class="holder-title">Managing Director</p>
    </header>
    <svg class="dot-row dot-row--contact" viewBox="0 0 300 26" aria-hidden="true">
      <circle class="dot" cx="6" cy="13" r="2"/><circle class="dot" cx="17" cy="13" r="3"/>
      <circle class="dot" cx="30" cy="13" r="4"/><circle class="dot" cx="45" cy="13" r="5"/>
      <circle class="dot" cx="62" cy="13" r="6"/>
      <circle class="dot" cx="86" cy="13" r="11"/>
      <rect class="glyph" x="82.5" y="7" width="7" height="12" rx="1.2"/>
      <circle class="dot" cx="112" cy="13" r="11"/>
      <path class="glyph" d="M107 9c1 5 4 8 9 9l2-2-3-2-1 1c-2-1-3-2-4-4l1-1-2-3z"/>
      <circle class="dot" cx="138" cy="13" r="11"/>
      <rect class="glyph" x="132" y="8.5" width="12" height="9" rx="1"/>
      <path class="glyph" d="M132 9l6 5 6-5"/>
      <circle class="dot" cx="164" cy="13" r="11"/>
      <circle class="glyph" cx="164" cy="13" r="6"/>
      <path class="glyph" d="M158 13h12M164 7c-3 3-3 9 0 12M164 7c3 3 3 9 0 12"/>
      <circle class="dot" cx="188" cy="13" r="6"/><circle class="dot" cx="205" cy="13" r="5"/>
      <circle class="dot" cx="220" cy="13" r="4"/><circle class="dot" cx="233" cy="13" r="3"/>
      <circle class="dot" cx="245" cy="13" r="2.5"/><circle class="dot" cx="256" cy="13" r="2"/>
    </svg>
    <ul class="contact-list">
      <li>(512) 404-3817</li>
      <li>(512) 404-2290</li>
      <li>info@fenmoor.com</li>
      <li>www.fenmoor.com</li>
    </ul>
    <svg class="dot-row dot-row--address" viewBox="0 0 300 26" aria-hidden="true">
      <circle class="dot" cx="10" cy="13" r="2"/><circle class="dot" cx="22" cy="13" r="2.5"/>
      <circle class="dot" cx="35" cy="13" r="3"/><circle class="dot" cx="49" cy="13" r="4"/>
      <circle class="dot" cx="65" cy="13" r="5"/><circle class="dot" cx="83" cy="13" r="6"/>
      <circle class="dot" cx="102" cy="13" r="6.5"/><circle class="dot" cx="122" cy="13" r="7"/>
      <circle class="dot" cx="148" cy="13" r="11"/>
      <path class="glyph" d="M148 19c-3-4-5-6-5-9a5 5 0 0 1 10 0c0 3-2 5-5 9z"/>
      <circle class="glyph" cx="148" cy="10" r="1.6"/>
      <circle class="dot" cx="174" cy="13" r="7"/><circle class="dot" cx="194" cy="13" r="6.5"/>
      <circle class="dot" cx="213" cy="13" r="6"/><circle class="dot" cx="230" cy="13" r="5"/>
      <circle class="dot" cx="245" cy="13" r="4"/><circle class="dot" cx="258" cy="13" r="3"/>
      <circle class="dot" cx="270" cy="13" r="2.5"/><circle class="dot" cx="281" cy="13" r="2"/>
    </svg>
    <address class="address">1840 Alder Crest Rd. Suite 310<br>Austin, TX 78701</address>
  </article>

  <article class="card card--greek" lang="el">
    <div class="brand-field" role="img" aria-label="Απαλό φόντο επωνυμίας"></div>
    <div class="wordmark">
      <div class="wordmark-lockup">
        <span class="wordmark-square"></span>
        <div class="wordmark-text">
          <span class="wordmark-name">Fenmoor</span>
          <span class="wordmark-sub">Σύμβουλοι</span>
        </div>
      </div>
    </div>
    <header class="holder">
      <h2 class="holder-name">Ντάρια Βέλκοβα</h2>
      <p class="holder-title">Διευθύνουσα Σύμβουλος</p>
    </header>
    <svg class="dot-row dot-row--contact" viewBox="0 0 300 26" aria-hidden="true">
      <circle class="dot" cx="6" cy="13" r="2"/><circle class="dot" cx="17" cy="13" r="3"/>
      <circle class="dot" cx="30" cy="13" r="4"/><circle class="dot" cx="45" cy="13" r="5"/>
      <circle class="dot" cx="62" cy="13" r="6"/>
      <circle class="dot" cx="86" cy="13" r="11"/>
      <rect class="glyph" x="82.5" y="7" width="7" height="12" rx="1.2"/>
      <circle class="dot" cx="112" cy="13" r="11"/>
      <path class="glyph" d="M107 9c1 5 4 8 9 9l2-2-3-2-1 1c-2-1-3-2-4-4l1-1-2-3z"/>
      <circle class="dot" cx="138" cy="13" r="11"/>
      <rect class="glyph" x="132" y="8.5" width="12" height="9" rx="1"/>
      <path class="glyph" d="M132 9l6 5 6-5"/>
      <circle class="dot" cx="164" cy="13" r="11"/>
      <circle class="glyph" cx="164" cy="13" r="6"/>
      <path class="glyph" d="M158 13h12M164 7c-3 3-3 9 0 12M164 7c3 3 3 9 0 12"/>
      <circle class="dot" cx="188" cy="13" r="6"/><circle class="dot" cx="205" cy="13" r="5"/>
      <circle class="dot" cx="220" cy="13" r="4"/><circle class="dot" cx="233" cy="13" r="3"/>
      <circle class="dot" cx="245" cy="13" r="2.5"/><circle class="dot" cx="256" cy="13" r="2"/>
    </svg>
    <ul class="contact-list">
      <li>(512) 404-3817</li>
      <li>(512) 404-2290</li>
      <li>info@fenmoor.com</li>
      <li>www.fenmoor.com</li>
    </ul>
    <svg class="dot-row dot-row--address" viewBox="0 0 300 26" aria-hidden="true">
      <circle class="dot" cx="10" cy="13" r="2"/><circle class="dot" cx="22" cy="13" r="2.5"/>
      <circle class="dot" cx="35" cy="13" r="3"/><circle class="dot" cx="49" cy="13" r="4"/>
      <circle class="dot" cx="65" cy="13" r="5"/><circle class="dot" cx="83" cy="13" r="6"/>
      <circle class="dot" cx="102" cy="13" r="6.5"/><circle class="dot" cx="122" cy="13" r="7"/>
      <circle class="dot" cx="148" cy="13" r="11"/>
      <path class="glyph" d="M148 19c-3-4-5-6-5-9a5 5 0 0 1 10 0c0 3-2 5-5 9z"/>
      <circle class="glyph" cx="148" cy="10" r="1.6"/>
      <circle class="dot" cx="174" cy="13" r="7"/><circle class="dot" cx="194" cy="13" r="6.5"/>
      <circle class="dot" cx="213" cy="13" r="6"/><circle class="dot" cx="230" cy="13" r="5"/>
      <circle class="dot" cx="245" cy="13" r="4"/><circle class="dot" cx="258" cy="13" r="3"/>
      <circle class="dot" cx="270" cy="13" r="2.5"/><circle class="dot" cx="281" cy="13" r="2"/>
    </svg>
    <address class="address">Οδός Άλντερ Κρεστ 1840, Γραφείο 310<br>Ώστιν, Τέξας 78701, ΗΠΑ</address>
  </article>

</main>
</body>
</html>
```